Business Card for Cedar Ridge Home Inspections

Very professional card that has the same logo as in logo project with simple info listed below.

Colors are Black, Red, White Silver and Gold

Reason: The extension is to run concurrently with the logo project.

Target Market(s)

Real Estate Industry Professionals

Industry/Entity Type

Business

Font styles to use
Serif

Requirements
Must have
• Logo only on front.
Company name , inspector name, company website, company phone on bck

```html
<!DOCTYPE html>
<html lang="en">
<head>
<meta charset="utf-8">
<title>Cedar Ridge Home Inspections – Business Card</title>
<link href="https://fonts.googleapis.com/css2?family=Lato:wght@400;700&display=swap" rel="stylesheet">
<style>
  :root {
    --page: #ffffff;
    --card: #000000;
    --red: #d42027;
    --white: #ffffff;
    --grey: #8a8a8a;
    --sky-top: #1a0d06;
    --sky-glow: #5a3a12;
    --lights: #c9a24a;
  }
  html, body {
    margin: 0;
    width: 872px;
    height: 1200px;
    overflow: hidden;
    background: var(--page);
    font-family: "Lato", Arial, sans-serif;
  }
  .canvas { position: relative; width: 872px; height: 1200px; }
  .card {
    position: absolute;
    left: 111px;
    width: 659px;
    height: 405px;
    background: var(--card);
    overflow: hidden;
  }
  .card--front { top: 104px; }
  .card--back { top: 701px; }

  .skyline-photo {
    position: absolute;
    left: 0; top: 0;
    width: 100%; height: 250px;
    background:
      linear-gradient(180deg, rgba(0,0,0,0) 55%, var(--card) 100%),
      linear-gradient(180deg, var(--sky-top) 0%, #2a1708 35%, var(--sky-glow) 62%, #2b1c0c 78%, var(--card) 100%);
  }
  .skyline-photo::after {
    content: "";
    position: absolute;
    left: 0; right: 0; top: 60px; height: 140px;
    background: radial-gradient(ellipse at 50% 60%, rgba(201,162,74,0.35), rgba(0,0,0,0) 70%);
  }

  .brand {
    position: absolute;
    display: flex;
    align-items: center;
    gap: 10px;
    color: var(--red);
    font-weight: 700;
    font-size: 15px;
    letter-spacing: 3px;
    text-transform: uppercase;
    line-height: 1.25;
  }
  .brand__mark {
    width: 14px; height: 14px;
    background: var(--red);
    flex: none;
  }
  .card--front .brand { left: 44px; top: 290px; }
  .card--back .brand { left: 50%; transform: translateX(-50%); top: 130px; white-space: nowrap; }

  .contact {
    position: absolute;
    right: 44px;
    top: 268px;
    text-align: right;
  }
  .contact__name {
    margin: 0 0 10px;
    color: var(--white);
    font-weight: 700;
    font-size: 20px;
    letter-spacing: 0.2px;
  }
  .contact__line {
    display: flex;
    justify-content: flex-end;
    align-items: center;
    gap: 6px;
    margin: 0 0 8px;
    color: var(--grey);
    font-size: 12.5px;
  }
  .contact__line svg { width: 12px; height: 12px; fill: var(--white); }

  .band-rule {
    position: absolute; left: 0; width: 100%; height: 8px;
    background: var(--white);
  }
  .band-rule--top { top: 192px; }
  .band-rule--bottom { top: 271px; }
  .web-band {
    position: absolute; left: 0; top: 200px;
    width: 100%; height: 71px;
    background: var(--red);
    display: flex; align-items: center; justify-content: center;
    color: var(--white);
    font-size: 12.5px;
    letter-spacing: 2.4px;
    text-transform: uppercase;
  }
</style>
</head>
<body>
<div class="canvas">
  <section class="card card--front">
    <div class="skyline-photo" role="img" aria-label="Night photograph of a city skyline with lit towers reflected in water"></div>
    <div class="brand">
      <span class="brand__mark"></span>
      <span>Cedar Ridge<br>Home Inspections</span>
    </div>
    <div class="contact">
      <p class="contact__name">DAN MERCER</p>
      <p class="contact__line">404-555-0187
        <svg viewBox="0 0 12 12" aria-hidden="true"><path d="M1 4c0-2 2-3 5-3s5 1 5 3v1H8.5V3.8h-5V5H1zM3 6h6l1.5 5h-9z"/></svg>
      </p>
      <p class="contact__line">dm@CRhomeinspections.com
        <svg viewBox="0 0 12 12" aria-hidden="true"><path d="M0 2h12v8H0z" fill="#fff"/><path d="M0.5 2.5 6 7l5.5-4.5" fill="none" stroke="#000" stroke-width="1"/></svg>
      </p>
    </div>
  </section>

  <section class="card card--back">
    <div class="brand">
      <span class="brand__mark"></span>
      <span>Cedar Ridge<br>Home Inspections</span>
    </div>
    <div class="band-rule band-rule--top"></div>
    <div class="web-band">www.CRhomeinspections.com</div>
    <div class="band-rule band-rule--bottom"></div>
  </section>
</div>
</body>
</html>
```